Professional banners for an eyewear company

I have 3 images which need to be made into banners. Size 990 x 370, with a 10 pixel white border at top and bottom of banner.

They all need to be adjusted to make the colours better and less bright.
All will need some writing written on them with a nice serif font.

Banner 1 text: Handcrafted luxury eyewear, with a purpose...
Banner 2 text: Half of our profits go to help malnourished children in India
Banner 3 text: 10% of your first order, use code: First Order

On our homepage these 3 banners will alternate, so they need to look good together.

Tips
Please take a look at the banners on the lunvoreck.com homepage, this is kind of how I want the text to be displayed, and they use good colours.

The backgrounds on Banners 2 & 3 can be changed.
Banner 3 background if you can change to a nice colour, as per lunvoreck.com homepage.
Updates

Hi, just a quick update, thank you for all the designs submitted so far, please keep in mind that the brand is a luxury high-end brand so designs will need to reflect this.

Industry/Entity Type

Eyewear

```html
<!DOCTYPE html>
<html lang="en">
<head>
<meta charset="utf-8">
<title>First Order Offer Banner</title>
<link href="https://fonts.googleapis.com/css2?family=Bodoni+Moda:opsz,wght@6..96,400&family=Macondo&display=swap" rel="stylesheet">
<style>
  :root {
    --frame-white: #ffffff;
    --sky-cyan: #1ff0ff;
    --sky-cyan-soft: #52e4fb;
    --ink-black: #0a0a0a;
    --hair-auburn: #b86a3e;
    --skin-warm: #efc9b4;
  }
  * { margin: 0; padding: 0; box-sizing: border-box; }
  html, body {
    width: 1200px;
    height: 448px;
    overflow: hidden;
    background: var(--frame-white);
  }
  .banner {
    position: relative;
    width: 1200px;
    height: 448px;
    background: var(--frame-white);
  }
  .banner__field {
    position: absolute;
    left: 0;
    top: 12px;
    width: 1200px;
    height: 424px;
    background: radial-gradient(ellipse at 62% 55%, var(--sky-cyan-soft) 0%, var(--sky-cyan) 70%);
    overflow: hidden;
  }
  .banner__model {
    position: absolute;
    left: 0;
    top: 0;
    width: 460px;
    height: 424px;
  }
  .offer__headline {
    position: absolute;
    right: 192px;
    top: 10px;
    white-space: nowrap;
    font-family: "Bodoni Moda", "Didot", serif;
    font-weight: 400;
    color: var(--ink-black);
    line-height: 0.8;
  }
  .offer__amount {
    font-size: 250px;
    letter-spacing: -4px;
    vertical-align: baseline;
  }
  .offer__suffix {
    display: inline-block;
    vertical-align: baseline;
    margin-left: 10px;
    text-align: center;
  }
  .offer__percent {
    display: block;
    font-size: 140px;
    line-height: 0.95;
  }
  .offer__off {
    display: block;
    font-size: 68px;
    line-height: 0.9;
    letter-spacing: 1px;
  }
  .offer__terms {
    position: absolute;
    left: 380px;
    width: 830px;
    top: 262px;
    text-align: center;
    white-space: nowrap;
    font-family: "Macondo", serif;
    font-size: 58px;
    line-height: 68px;
    color: var(--ink-black);
  }
</style>
</head>
<body>
  <div class="banner">
    <div class="banner__field">
      <svg class="banner__model" role="img" aria-label="Photo of a red-haired woman in dark sunglasses with an excited open-mouthed expression" viewBox="0 0 460 424">
        <defs>
          <linearGradient id="modelTones" x1="0" y1="0" x2="1" y2="0.3">
            <stop offset="0" stop-color="var(--hair-auburn)"/>
            <stop offset="0.35" stop-color="var(--skin-warm)"/>
            <stop offset="0.7" stop-color="var(--skin-warm)"/>
            <stop offset="1" stop-color="var(--hair-auburn)"/>
          </linearGradient>
        </defs>
        <path d="M0 0 H436 C450 90 440 170 405 260 C385 300 375 360 380 424 H0 Z" fill="url(#modelTones)"/>
      </svg>
      <h1 class="offer__headline"><span class="offer__amount">10</span><span class="offer__suffix"><span class="offer__percent">%</span><span class="offer__off">OFF</span></span></h1>
      <p class="offer__terms">your first order,<br>use code: First Order</p>
    </div>
  </div>
</body>
</html>
```